Dust N Gone! Cleaning needs a flyer!

We have started a cleaning business DUST N GONE! Cleaning, and had a new logo design for it.
We would like a flyer designed to present to businesses that represents our professionalism, quality of service, security and value for money.
We would like a flyer that we can present to both our residential clients and business owners alike.
We will use this flyer for the next 2 years without having to make changes.
I'm happy for the designer to come up with their own wording if necessary.
Updates

Hello everyone!

In addition to the information I have already provided, please see below for more information to be included on the design for our flyer.

Thank you in advance.

Don’t read this unless your current cleaners are AMAZING!

Are you still reading? Now for the good news! Announcing the arrival of the amazing cleaning team of Dust N Gone! Cleaning. They’re the BEST in the Wimmera and we personally guarantee it.

We offer an ultimate service that NO other cleaning company in the Wimmera can offer; high quality cleaning of your home or business, carpet dry cleaning and pest control. All of these services can be completed at a time that is most convenient to you.

From wiping benches to washing windows, from dusting skirting boards to dry cleaning your carpets, from bathrooms to bugs, we really are your ONE stop shop.

Why choose the greatest cleaning company in the Wimmera?

For over 18 years, we have built a reputation on honesty and trust in the residential and commercial services. Our business is to know what people expect when we walk in to your home or business.

With our vast experience and knowledge, we know how to find the best people for the job, how to identify the best products for the clean, we use the newest of technology and equipment and have the best attitudes in town.

Local people, local business that you can rely on because we are also Dust N Gone! Pest Control & Fibrela all rolled in to your ONE stop shop for residential services.

Call us to discuss how we can give you the quality you demand.

Residential Cleaning                                                       Commercial Cleaning                                     

General house cleaning                                                  Business Premises          

Home help                                                                         Vacated properties

Rental vacancies                                                               Schools

Post renovation cleans                                                     Motels/Hotels

 

                                   

Target Market(s)

Business owners, commercial properties, home owners (women aged between 30 - 80y/o)

Industry/Entity Type

Residential

Requirements
Must have
• Incorporate our logo and colours.
Double sided.
Images of interiors of both home & office.
Catch phrase: "You demand quality ..... we guarantee it!"
Address: 22-26 Wattlegum St, Horsham VIC 3400
Phone: 1300 482 316
ABN: 47 308 562 194
We complete the ususal cleaning such as:
General House cleaning
Commercial Cleaning
Rental Properties
Business Premises
Other services we offer is:
Carpet dry cleaning
Upholstery cleaning
Dust N Gone! Mite Chasers pest control
Window cleaning.

```html
<!DOCTYPE html>
<html lang="en">
<head>
<meta charset="utf-8">
<title>Dust N Gone! Cleaning – Flyer</title>
<link href="https://fonts.googleapis.com/css2?family=Open+Sans:wght@400;600;700;800&display=swap" rel="stylesheet">
<style>
  :root {
    --pink: #e21fd0;
    --pink-soft: #f4b3ee;
    --pink-pale: #fbe3f8;
    --black: #050505;
    --white: #ffffff;
    --ink: #111111;
    --canvas: #f6eaf5;
  }
  * { box-sizing: border-box; margin: 0; padding: 0; }
  html, body { width: 1200px; height: 900px; overflow: hidden; }
  body {
    background: var(--canvas);
    font-family: "Open Sans", Arial, sans-serif;
    position: relative;
  }
  .flyer-page {
    position: absolute;
    top: 120px;
    width: 480px;
    height: 660px;
    overflow: hidden;
    box-shadow: 0 6px 22px rgba(80, 20, 70, 0.25);
  }
  .flyer-front { left: 90px; background: var(--black); }
  .flyer-back {
    left: 630px;
    background: linear-gradient(180deg, var(--pink-pale) 0%, var(--white) 22%, var(--white) 62%, var(--pink-soft) 100%);
  }
  .page-art { position: absolute; inset: 0; width: 100%; height: 100%; }

  /* Front */
  .tagline-pill {
    position: absolute;
    top: 42px; left: 28px;
    padding: 9px 22px;
    border-radius: 24px;
    background: linear-gradient(180deg, #f47be9 0%, var(--pink) 100%);
    color: var(--white);
    font-size: 21px;
    font-weight: 400;
    white-space: nowrap;
  }
  .brand-name {
    font-weight: 800;
    color: var(--pink);
    letter-spacing: 0.5px;
  }
  .front-brand {
    position: absolute;
    top: 470px; left: 0; right: 0;
    text-align: center;
    font-size: 34px;
    line-height: 1.15;
  }
  .front-contact {
    position: absolute;
    top: 568px; left: 0; right: 0;
    text-align: center;
    color: var(--white);
    font-size: 15px;
  }
  .front-contact .label { color: var(--pink); font-weight: 700; }
  .front-contact span + span { margin-left: 16px; }

  /* Back */
  .back-brand {
    position: absolute;
    top: 50px; left: 40px;
    width: 230px;
    font-size: 27px;
    line-height: 1.15;
  }
  .back-contact {
    position: absolute;
    top: 32px; left: 300px;
    font-size: 10.5px;
    font-weight: 700;
    color: var(--ink);
    line-height: 1.4;
  }
  .back-contact .label { color: var(--pink); }
  .back-contact .address { margin-top: 12px; }
  .service-list {
    position: absolute;
    left: 62px;
    list-style: none;
    font-size: 15px;
    font-weight: 700;
    color: var(--ink);
    line-height: 20px;
  }
  .service-list li::before {
    content: "";
    display: inline-block;
    width: 7px; height: 7px;
    border-radius: 50%;
    background: var(--pink);
    margin: 0 10px 2px -17px;
    vertical-align: middle;
  }
  .core-services { top: 434px; }
  .extra-services { top: 560px; }
  .extra-heading {
    position: absolute;
    top: 522px; left: 42px;
    padding: 4px 18px;
    border-radius: 16px;
    background: linear-gradient(180deg, #f47be9 0%, var(--pink) 100%);
    color: var(--white);
    font-size: 14px;
    font-weight: 700;
    line-height: 20px;
  }
</style>
</head>
<body>

  <section class="flyer-page flyer-front" aria-label="Flyer front">
    <svg class="page-art" viewBox="0 0 480 660">
      <defs>
        <linearGradient id="homeTones" x1="0" y1="0" x2="0" y2="1">
          <stop offset="0" stop-color="#f3efe8"/>
          <stop offset="0.45" stop-color="#e2d2bc"/>
          <stop offset="0.75" stop-color="#b98a5c"/>
          <stop offset="1" stop-color="#7a4a2a"/>
        </linearGradient>
      </defs>
      <path role="img" aria-label="Photo of a bright open-plan home kitchen and living room with timber floors and a dining table"
            d="M0 0 H480 V390 C330 350 150 300 0 305 Z" fill="url(#homeTones)"/>
      <path d="M170 70 C260 62 380 60 480 52 V96 C380 94 260 92 170 96 Z" fill="var(--black)"/>
      <path d="M0 305 C150 300 330 350 480 390 V405 C330 375 150 330 0 335 Z" fill="var(--pink)"/>
    </svg>
    <div class="tagline-pill">You demand quality...we guarantee it!</div>
    <div class="front-brand brand-name">DUST N GONE!<br>Cleaning</div>
    <p class="front-contact">
      <span><span class="label">P.</span> 1300 482 316</span>
      <span><span class="label">F.</span> 03 5391 6048</span>
    </p>
  </section>

  <section class="flyer-page flyer-back" aria-label="Flyer back">
    <svg class="page-art" viewBox="0 0 480 660">
      <defs>
        <linearGradient id="officeTones" x1="0" y1="0" x2="1" y2="1">
          <stop offset="0" stop-color="#cfc8bb"/>
          <stop offset="0.5" stop-color="#e8dccb"/>
          <stop offset="1" stop-color="#8d8a86"/>
        </linearGradient>
      </defs>
      <path d="M0 195 C140 160 320 140 480 150 V168 C320 162 140 182 0 215 Z" fill="var(--pink)"/>
      <path role="img" aria-label="Photo of a modern office with timber desks, drawers and black swivel chairs"
            d="M0 215 C140 182 320 162 480 168 V360 C330 395 170 415 0 410 Z" fill="url(#officeTones)"/>
      <path d="M0 410 C170 415 330 395 480 360 V378 C330 418 170 435 0 425 Z" fill="var(--pink)"/>
    </svg>
    <div class="back-brand brand-name">DUST N GONE!<br>Cleaning</div>
    <div class="back-contact">
      <div><span class="label">P.</span> 1300 482 316</div>
      <div><span class="label">F.</span> 03 5391 6048</div>
      <div><span class="label">ABN:</span> 47 308 562 194</div>
      <div class="address">22-26 Wattlegum St<br>Horsham VIC 3400</div>
    </div>
    <ul class="service-list core-services">
      <li>General House cleaning</li>
      <li>Commercial Cleaning</li>
      <li>Rental Properties</li>
      <li>Business Premises</li>
    </ul>
    <div class="extra-heading">Other services we offer:</div>
    <ul class="service-list extra-services">
      <li>Carpet Dry Cleaning</li>
      <li>Upholstery Cleaning</li>
      <li>Dust N Gone! Mite Chasers Pest Control</li>
      <li>Window Cleaning</li>
    </ul>
  </section>

</body>
</html>
```